KORVEL Group Pty Ltd. Website and Domain

www.korvelgroup.com.au

require email addresses setup.

Info@korvelgroup.com.au
accounts@korvelgroup.com.au
peter.walsby@korvelgroup.com.au
roland.hughes@korvelgroup.com.au

Website should promote commercial and domestic electrical services, audio visual services and data and fibre installations.

similar to my mates site www.bvplanet.com.au

Website needs to promote professionalism, electrical/electrician, audio visual and data/fibre cabling installations.

promote environmental friendly imaginary.

```html
<!DOCTYPE html>
<html lang="en">
<head>
<meta charset="utf-8">
<title>KORVEL Group Pty Ltd. — Electrical, Audio Visual and Data</title>
<link href="https://fonts.googleapis.com/css2?family=Arimo:wght@400;700&family=PT+Serif&family=PT+Sans:wght@400;700&display=swap" rel="stylesheet">
<style>
:root{
  --blue:#2f9bd0;
  --green:#a6ce39;
  --ink:#1a1a1a;
  --grey-band:#ebebeb;
  --contact-band:#dcdcdc;
  --footer:#141414;
  --white:#ffffff;
}
*{margin:0;padding:0;box-sizing:border-box}
html,body{width:1200px;height:2738px;overflow:hidden;background:var(--white)}
body{position:relative;font-family:"Arimo",Arial,sans-serif;color:var(--ink)}
.abs{position:absolute}

/* hero */
.hero{left:0;top:0;width:1200px;height:691px;
  background:radial-gradient(ellipse at 50% 25%,#8a5a2a 0%,#4a2f1c 35%,#2a1d15 70%,#1c1512 100%)}
.brand{left:21px;top:26px;display:flex;align-items:center;gap:12px}
.brand-mark{width:60px;height:60px;border-radius:50%;border:5px solid var(--green)}
.brand-name{font-weight:700;font-size:42px;color:var(--blue);letter-spacing:1px}
.nav{top:45px;font-weight:700;font-size:16px;color:var(--blue);letter-spacing:1px}
.hero-title{left:0;width:1200px;text-align:center;font-weight:700;font-size:51px;line-height:59px;top:281px;text-transform:uppercase}
.g{color:var(--green)}.b{color:var(--blue)}
.hero-btn{left:478px;top:448px;width:249px;height:59px;background:var(--green);border-radius:5px;
  font-weight:700;font-size:28px;color:#111;display:flex;align-items:center;justify-content:center;letter-spacing:1px}

/* about */
.accent-bar{width:7px;background:var(--green)}
.section-heading{font-weight:700;font-size:28px;color:var(--blue);letter-spacing:1px}
.about-text{left:116px;top:797px;width:460px;font-size:15px;line-height:24.9px}
.btn-blue{background:var(--blue);color:var(--white);font-size:15px;display:flex;align-items:center;justify-content:center}
.photo{display:block}
.photo-house{background:linear-gradient(180deg,#6f86d6 0%,#a7a9d0 35%,#b08a5a 60%,#6c6a5f 80%,#4a4b3e 100%)}
.photo-house-day{background:linear-gradient(180deg,#8fa9c8 0%,#c2c6c4 35%,#8c8a80 65%,#9a958c 100%)}
.photo-house-night{background:linear-gradient(180deg,#2a3c6c 0%,#1d2a48 40%,#7a5a30 65%,#1a2a40 100%)}

/* services */
.services{left:0;top:1112px;width:1200px;height:536px;background:var(--grey-band)}
.services-intro{left:0;width:1200px;top:1189px;text-align:center;font-size:15px;line-height:25px}
.card{width:220px;height:341px;color:var(--white)}
.card-bulb{background:radial-gradient(ellipse at 50% 35%,#2c3540 0%,#111418 60%,#07080a 100%)}
.card-av{background:linear-gradient(180deg,#1c1c1c 0%,#2a2a2a 55%,#141414 100%)}
.card-data{background:radial-gradient(ellipse at 50% 20%,#3b2a2a 0%,#1d1a1a 55%,#0c0c0c 100%)}
.card-icon{position:absolute;left:24px;top:94px}
.card-title{position:absolute;left:25px;top:145px;font-size:19px}
.card-text{position:absolute;left:25px;top:176px;font-size:13px;line-height:22px;width:190px}
.card-btn{position:absolute;right:0;bottom:0;width:124px;height:34px}

/* work */
.work-heading{left:0;width:1216px;text-align:center;top:1688px}

/* contact */
.contact{left:0;top:2163px;width:1200px;height:375px;background:var(--contact-band)}
.photo-bulbs{left:116px;top:2167px;width:475px;height:365px;
  background:radial-gradient(ellipse at 55% 45%,#7a4a22 0%,#3c2818 45%,#1f1812 100%)}
.contact-title{left:162px;top:2314px;font-weight:700;font-size:30px;line-height:34px;text-transform:uppercase}
.form-panel{left:591px;top:2167px;width:509px;height:361px;background:var(--white)}
.form-title{left:591px;width:498px;top:2183px;text-align:center;font-family:"PT Serif",Georgia,serif;font-size:15px;color:#444}
.field-label{left:642px;font-family:"PT Sans",Arial,sans-serif;font-weight:700;font-size:10px;color:#333}
.field-label small{font-weight:400;font-size:8px;color:#666}
.field{left:642px;width:388px;border:1px solid #e2e2e2;border-radius:3px;background:var(--white)}
.submit{left:642px;top:2494px;width:49px;height:23px;background:#1d7ea8;color:var(--white);border-radius:2px;
  font-family:"PT Sans",Arial,sans-serif;font-weight:700;font-size:8px;display:flex;align-items:center;justify-content:center}

/* footer */
.footer{left:0;top:2538px;width:1200px;height:200px;background:var(--footer)}
.footer-text{font-size:13px;line-height:22.5px;color:var(--white)}
</style>
</head>
<body>

<!-- hero -->
<section class="abs hero" role="img" aria-label="Row of glowing vintage filament light bulbs hanging in front of a dark brick wall"></section>
<div class="abs brand">
  <span class="brand-mark"></span>
  <span class="brand-name">KORVEL</span>
</div>
<nav>
  <span class="abs nav" style="left:716px">ABOUT US</span>
  <span class="abs nav" style="left:847px">OUR SERVICES</span>
  <span class="abs nav" style="left:1016px">CONTACT US</span>
</nav>
<h1 class="abs hero-title">
  <span class="g">For all your </span><span class="b">electrical,</span><br>
  <span class="b">audio, visual and </span><span class="b">data </span><span class="g">needs</span>
</h1>
<a class="abs hero-btn">CONTACT US</a>

<!-- about -->
<div class="abs accent-bar" style="left:71px;top:751px;height:103px"></div>
<h2 class="abs section-heading" style="left:116px;top:750px">ABOUT US</h2>
<p class="abs about-text">Lorem ipsum dolor sit amet, consectetur adipiscing elit, sed do eiusmod tempor incididunt ut labore et dolore magna aliqua. Quis ipsum suspendisse ultrices gravida. Risus commodo viverra maecenas accumsan lacus vel facilisis. Lorem ipsum dolor sit amet, consectetur adipiscing elit, sed do eiusmod tempor incididunt ut labore et dolore magna aliqua. Quis ipsum suspendisse ultrices gravida. Risus commodo viverra maecenas accumsan lacus vel facilisis.</p>
<a class="abs btn-blue" style="left:116px;top:1021px;width:124px;height:35px">Learn More</a>
<div class="abs photo photo-house" style="left:596px;top:715px;width:530px;height:353px" role="img" aria-label="Modern home courtyard lit with warm exterior lighting at dusk"></div>

<!-- services -->
<section class="abs services"></section>
<h2 class="abs section-heading" style="left:0;width:1186px;text-align:center;top:1139px">OUR SERVICES</h2>
<p class="abs services-intro">Lorem ipsum dolor sit amet, consectetur adipiscing elit, sed do eiusmod tempor incididunt ut<br>labore et dolore magna aliqua. Quis ipsum suspendisse ultrices gravida. Risus commodo viverra</p>

<div class="abs card card-bulb" style="left:229px;top:1262px" role="img" aria-label="Close-up of a filament light bulb on a dark background">
  <svg class="card-icon" width="36" height="48" viewBox="0 0 36 48" fill="none" stroke="#a6ce39" stroke-width="2.5">
    <path d="M18 3a14 14 0 0 0-8 25c2 2 3 4 3 7h10c0-3 1-5 3-7A14 14 0 0 0 18 3z"/>
    <path d="M13 40h10M14 45h8M18 35V20l-4-4M18 20l4-4"/>
  </svg>
  <div class="card-title">Electrical Services</div>
  <div class="card-text">Lorem ipsum dolor sit amet, consectetur adipiscing elit, sed do eiusmod tempor</div>
  <a class="card-btn btn-blue">Learn More</a>
</div>

<div class="abs card card-av" style="left:494px;top:1263px" role="img" aria-label="Studio microphone and mixing desk in a dim recording room">
  <svg class="card-icon" style="left:60px" width="44" height="50" viewBox="0 0 44 50" fill="#a6ce39">
    <path d="M22 2c4 8 14 14 14 28a14 14 0 0 1-28 0c0-8 5-12 7-18 2 4 2 8 5 10 0-8 0-14 2-20z"/>
  </svg>
  <div class="card-title" style="left:25px">Audio Visual</div>
  <div class="card-text" style="left:27px">Lorem ipsum dolor sit amet, consectetur adipiscing elit, sed do eiusmod tempor</div>
  <a class="card-btn btn-blue" style="width:124px;right:10px">Learn More</a>
</div>

<div class="abs card card-data" style="left:758px;top:1260px" role="img" aria-label="Tangle of colourful data and fibre cables">
  <svg class="card-icon" style="left:13px" width="44" height="42" viewBox="0 0 44 42" fill="none" stroke="#a6ce39" stroke-width="3">
    <path d="M5 12l7 18h20l7-18-10 8-7-14-7 14z"/>
    <path d="M10 36h24"/>
  </svg>
  <div class="card-title" style="left:13px">Data and Fibre</div>
  <div class="card-text" style="left:13px">Lorem ipsum dolor sit amet, consectetur adipiscing elit, sed do eiusmod tempor</div>
  <a class="card-btn btn-blue">Learn More</a>
</div>

<!-- our work -->
<h2 class="abs section-heading work-heading">OUR WORK</h2>
<div class="abs photo photo-house" style="left:65px;top:1743px;width:722px;height:382px" role="img" aria-label="Illuminated modern home and paved courtyard at twilight"></div>
<div class="abs photo photo-house-day" style="left:805px;top:1743px;width:353px;height:186px" role="img" aria-label="Stone-fronted house entrance with lit windows"></div>
<div class="abs photo photo-house-night" style="left:805px;top:1938px;width:353px;height:187px" role="img" aria-label="Two-storey house with pool lit up at night"></div>

<!-- contact -->
<section class="abs contact"></section>
<div class="abs photo-bulbs" role="img" aria-label="Hanging filament light bulbs against a brick wall"></div>
<h2 class="abs contact-title">
  <span class="g">For all your</span><br>
  <span class="b">electrical, audio,</span><br>
  <span class="b">visual and data </span><span class="g">needs</span>
</h2>
<div class="abs form-panel"></div>
<div class="abs form-title">Get in Touch</div>
<label class="abs field-label" style="top:2221px">Name <small>(required)</small></label>
<div class="abs field" style="top:2240px;height:20px"></div>
<label class="abs field-label" style="top:2280px">Email <small>(required)</small></label>
<div class="abs field" style="top:2298px;height:20px"></div>
<label class="abs field-label" style="top:2339px">Message</label>
<div class="abs field" style="top:2357px;height:114px"></div>
<a class="abs submit">Submit</a>

<!-- footer -->
<footer class="abs footer"></footer>
<div class="abs accent-bar" style="left:53px;top:2564px;height:101px"></div>
<h2 class="abs section-heading" style="left:97px;top:2563px">ABOUT US</h2>
<p class="abs footer-text" style="left:97px;top:2607px">Lorem ipsum dolor sit amet, consectetur<br>adipiscing elit, sed do eiusmod tempor<br>incididunt ut labore et dolore magna aliqua.</p>

<div class="abs accent-bar" style="left:469px;top:2570px;height:101px"></div>
<h2 class="abs section-heading" style="left:512px;top:2569px">CONTACT US</h2>
<p class="abs footer-text" style="left:516px;top:2607px">Lorem ipsum dolor<br>sit amet, consectetur adipiscing<br>&nbsp;elit, sed do eiusmod tempor incididunt ut</p>

<div class="abs accent-bar" style="left:847px;top:2570px;height:101px"></div>
<h2 class="abs section-heading" style="left:890px;top:2569px">STALK US</h2>
<p class="abs footer-text" style="left:894px;top:2607px">Linkora<br>Snapwell<br>Chirpline</p>

</body>
</html>
```